Project Manager Business Card for Top Architectural Firm

Update and design a stunning Senior Project Manager Business Card

MARCO T. DRUMMOND II
Senior Project Manager

H A L C Y O N
A R C H I T E C T U R E L L C.
www.HalcyonGrandEstates.example
4127 NW 52nd Ter. Suite 2308
Miami, FL 33148
C: (305) 555-0184
mdrummond.halcyongrandestates@mailbox.example

Looking to have the logo to be UV Spot ink printed and to be prominent.

Target Market(s)

High end real estate architecture construction

Industry/Entity Type

Architect

Contact Information for Business Card

MARCO T. DRUMMOND II
Senior Project Manager

H A L C Y O N
Miami, FL 33148
C: (305) 555-0184

Font styles to use
Sans Serif

Colors

Designer to choose colors to be used in the design.

Requirements
Must have
• Prominent Logo

```html
<!DOCTYPE html>
<html lang="en">
<head>
<meta charset="utf-8">
<title>Halcyon Architecture – Business Card</title>
<link href="https://fonts.googleapis.com/css2?family=Oswald:wght@300;600&family=Lato:wght@400&display=swap" rel="stylesheet">
<style>
  :root {
    --backdrop: #2d2d2d;
    --card: #262626;
    --card-edge: #1f1f1f;
    --spot-ink: #161616;
    --accent: #3b9bd8;
    --text: #f2f2f2;
    --muted: #dcdcdc;
  }
  html, body {
    margin: 0;
    padding: 0;
    width: 1200px;
    height: 959px;
    overflow: hidden;
    background: var(--backdrop);
  }
  .stage {
    position: relative;
    width: 1200px;
    height: 959px;
    background: radial-gradient(ellipse at 50% 40%, #363636 0%, var(--backdrop) 70%);
  }
  .card {
    position: absolute;
    left: 290px;
    width: 620px;
    height: 354px;
    background: var(--card);
    border: 1px solid var(--card-edge);
    box-sizing: border-box;
  }
  .card--front { top: 70px; }
  .card--back { top: 490px; }

  /* Front: brand name in spot ink */
  .brand {
    position: absolute;
    left: 0;
    right: 0;
    top: 72px;
    display: flex;
    flex-direction: column;
    align-items: center;
  }
  .brand__dot {
    width: 74px;
    height: 74px;
    border-radius: 50%;
    background: var(--accent);
    margin-bottom: 26px;
  }
  .brand__name,
  .brand__sub {
    font-family: 'Oswald', sans-serif;
    font-weight: 300;
    color: var(--spot-ink);
    margin: 0;
    line-height: 1;
  }
  .brand__name {
    font-size: 64px;
    letter-spacing: 14px;
    margin-right: -14px;
  }
  .brand__sub {
    font-size: 15px;
    letter-spacing: 9px;
    margin-top: 6px;
    margin-right: -9px;
  }

  /* Back: contact details */
  .card__dot {
    position: absolute;
    left: 36px;
    top: 34px;
    width: 58px;
    height: 58px;
    border-radius: 50%;
    background: var(--accent);
  }
  .contact {
    position: absolute;
    left: 0;
    right: 0;
    top: 112px;
    text-align: center;
    color: var(--text);
    font-family: 'Lato', sans-serif;
  }
  .contact__name {
    font-family: 'Oswald', sans-serif;
    font-weight: 600;
    font-size: 30px;
    letter-spacing: 2px;
    margin: 0;
    line-height: 1.1;
  }
  .contact__title {
    font-size: 18px;
    margin: 2px 0 12px;
    color: var(--muted);
  }
  .contact__line {
    font-size: 18px;
    margin: 2px 0;
    display: flex;
    justify-content: center;
    align-items: center;
    gap: 8px;
  }
  .contact__line svg { width: 16px; height: 16px; flex: none; }
  .contact__address {
    font-size: 20px;
    margin-top: 26px;
  }
</style>
</head>
<body>
<main class="stage">
  <section class="card card--front" aria-label="Card front">
    <div class="brand">
      <div class="brand__dot"></div>
      <p class="brand__name">HALCYON</p>
      <p class="brand__sub">ARCHITECTURE LLC.</p>
    </div>
  </section>

  <section class="card card--back" aria-label="Card back">
    <div class="card__dot"></div>
    <div class="contact">
      <h1 class="contact__name">MARCO T. DRUMMOND II</h1>
      <p class="contact__title">Senior Project Manager</p>
      <p class="contact__line">
        <svg viewBox="0 0 16 16" aria-hidden="true"><path fill="var(--accent)" d="M3.2 1.5l2.3-.4 1.3 3.3-1.5 1.2c.8 1.8 2.2 3.2 4 4l1.2-1.5 3.3 1.3-.4 2.3c-.2.8-.9 1.3-1.7 1.3C6.3 13 3 9.7 2 3.2c0-.8.5-1.5 1.2-1.7z"/></svg>
        (305) 555-0184
      </p>
      <p class="contact__line">
        <svg viewBox="0 0 16 16" aria-hidden="true"><rect x="1" y="3" width="14" height="10" fill="none" stroke="var(--accent)" stroke-width="1.4"/><path d="M1 3l7 6 7-6" fill="none" stroke="var(--accent)" stroke-width="1.4"/></svg>
        mdrummond.halcyongrandestates@mailbox.example
      </p>
      <p class="contact__line">
        <svg viewBox="0 0 16 16" aria-hidden="true"><g fill="none" stroke="var(--accent)" stroke-width="1.2"><circle cx="8" cy="8" r="6.5"/><ellipse cx="8" cy="8" rx="3" ry="6.5"/><path d="M1.5 8h13M2.5 4.5h11M2.5 11.5h11"/></g></svg>
        www.HalcyonGrandEstates.example
      </p>
      <p class="contact__address">4127 NW 52nd Ter. Suite 2308, Miami, FL 33148</p>
    </div>
  </section>
</main>
</body>
</html>
```